Consulting company needs Business Cards - rough concept provided

I'm looking for someone to take our business card idea and make is slick and polished - to communicate our high-end, sophisticated, serious consulting business. We have a rough layout we did in-house. We are open to ideas on repo-ing elements, adjusting sizes, typefaces etc... within the general concept we've already come up with. We want it to be super-clean and sophisticated. We want to keep the white backgrounds, and blue brand colors. Our goal is to print with painted blue edges on thick cardstock. Thank you!!

```html
<!DOCTYPE html>
<html lang="en">
<head>
<meta charset="utf-8">
<title>Tall Otter Business Cards</title>
<link rel="stylesheet" href="https://fonts.googleapis.com/css2?family=Work+Sans:wght@300;400;600;700;900&display=swap">
<style>
  :root {
    --brand-blue: #0a8ad6;
    --rule-blue: #3fb8f0;
    --ink-grey: #8f9092;
    --soft-grey: #b9babc;
    --card-white: #ffffff;
    --backdrop: #d4d5d7;
  }
  * { box-sizing: border-box; margin: 0; padding: 0; }
  html, body {
    width: 1200px;
    height: 800px;
    overflow: hidden;
    background: var(--backdrop);
    font-family: "Work Sans", sans-serif;
  }
  .sheet {
    position: relative;
    width: 1200px;
    height: 800px;
    display: flex;
    align-items: center;
    justify-content: center;
    gap: 50px;
  }
  .card {
    position: relative;
    width: 530px;
    height: 303px;
    background: var(--card-white);
    border-bottom: 3px solid var(--brand-blue);
    border-right: 2px solid var(--brand-blue);
    box-shadow: 0 14px 28px rgba(0, 0, 0, 0.22);
    overflow: hidden;
  }

  /* Front */
  .brand-name {
    position: absolute;
    top: 34px;
    right: 34px;
    display: flex;
    align-items: center;
    gap: 10px;
    font-weight: 600;
    font-size: 30px;
    line-height: 1;
    color: var(--brand-blue);
  }
  .brand-dot {
    width: 14px;
    height: 14px;
    background: var(--brand-blue);
  }
  .contact {
    position: absolute;
    left: 34px;
    bottom: 30px;
  }
  .contact-name {
    font-weight: 700;
    font-size: 24px;
    color: var(--brand-blue);
    line-height: 1.1;
  }
  .contact-title {
    font-weight: 700;
    font-size: 14px;
    color: var(--ink-grey);
    letter-spacing: 0.3px;
    margin-top: 2px;
  }
  .contact-rule {
    width: 190px;
    height: 1.5px;
    background: var(--rule-blue);
    margin: 10px 0;
  }
  .contact-line {
    font-weight: 400;
    font-size: 13px;
    color: var(--ink-grey);
    line-height: 1.6;
    letter-spacing: 0.3px;
  }
  .contact-label {
    font-weight: 700;
    color: var(--brand-blue);
  }

  /* Back */
  .statement {
    position: absolute;
    left: 30px;
    right: 20px;
    top: 40px;
    font-weight: 300;
    font-size: 21px;
    line-height: 1.9;
    letter-spacing: 0.3px;
    word-spacing: 4px;
    color: var(--soft-grey);
    white-space: nowrap;
  }
  .statement-key {
    font-weight: 900;
    color: var(--brand-blue);
  }
</style>
</head>
<body>
  <main class="sheet">
    <section class="card card-front">
      <div class="brand-name"><span class="brand-dot"></span>Tall Otter</div>
      <div class="contact">
        <p class="contact-name">Dana Whitfield</p>
        <p class="contact-title">Brand Consultant</p>
        <div class="contact-rule"></div>
        <p class="contact-line">4820 Harbor Lane, Ste 210 Lakeview, CA 90210</p>
        <p class="contact-line"><span class="contact-label">P:</span> (555) 310 4827</p>
        <p class="contact-line"><span class="contact-label">E:</span> dana@tallotter.com</p>
      </div>
    </section>

    <section class="card card-back">
      <p class="statement">
        <span class="statement-key">We help</span> [target demographic] <span class="statement-key">achieve</span><br>
        [desired emotional outcome] <span class="statement-key">by</span> [our<br>
        unique approach] <span class="statement-key">because</span> [our brand<br>
        beliefs]
      </p>
    </section>
  </main>
</body>
</html>
```